TRENDY & MODERN BUSINESS CARD DESIGN for Media Company *

I need a minimalistic - clean - modern and professional business card layout and design for MEDIA & PHOTOGRAPHY STUDIO.

We do NOT have a logo, and not really looking for one - but rather excellent typography and design. We would consider the 3 as a focal point.

We do personal and commercial photography.

Target Market(s)

Personal and commercial photography clientele

Contact Information for Business Card

ZUB size - from zub.com / size guidelines are enclosed in the brief

Font styles to use
Sans Serif

Colors
f78f20
eda3c7
cee9f5
0555a3
e667a6
fbf289

Requirements
Must have
• Clean lines - Modern layout
Nice to have
• All blue background as an option - use color palette in brief please.
Should not have
• Old fashion fonts and regular fonts.

```html
<!DOCTYPE html>
<html lang="en">
<head>
<meta charset="utf-8">
<title>Lumen Arc Media — Business Card</title>
<link rel="stylesheet" href="https://fonts.googleapis.com/css2?family=Montserrat:wght@400;600;800&family=Work+Sans:wght@400;500&display=swap">
<style>
  :root {
    --backdrop: #1e1f22;
    --paper: #ffffff;
    --ink: #1b1b1b;
    --ink-soft: #3a3a3a;
    --brand-blue: #0555a3;
    --deep-blue: #0a4482;
    --stripe-blue: #0d3d72;
    --brand-yellow: #fbf289;
    --brand-pink: #eda3c7;
    --brand-orange: #f78f20;
    --tagline-blue: #2f5f9a;
  }
  * { box-sizing: border-box; margin: 0; padding: 0; }
  html, body {
    width: 1200px; height: 900px; overflow: hidden;
    background: var(--backdrop);
  }
  .sheet {
    width: 1200px; height: 900px;
    display: flex; align-items: center; justify-content: center; gap: 60px;
  }
  .card {
    width: 530px; height: 303px; position: relative; overflow: hidden;
    border-radius: 3px;
  }

  /* Back: contact side */
  .card--contact { background: var(--paper); color: var(--ink); font-family: "Work Sans", sans-serif; }
  .contact__name {
    position: absolute; left: 40px; top: 38px;
    font-family: "Montserrat", sans-serif; font-weight: 800; font-size: 24px; letter-spacing: .2px;
  }
  .contact__role { position: absolute; left: 40px; top: 72px; font-size: 14px; color: var(--ink-soft); }
  .contact__rule-short { position: absolute; left: 40px; top: 110px; width: 200px; height: 1px; background: var(--ink); }
  .contact__rule-long { position: absolute; left: 268px; top: 110px; width: 1px; height: 160px; background: var(--ink); }
  .contact__lines {
    position: absolute; left: 40px; top: 140px;
    font-size: 15px; line-height: 23px; color: var(--ink-soft);
  }
  .contact__address {
    position: absolute; left: 296px; bottom: 40px;
    font-size: 16px; line-height: 24px; color: var(--ink-soft);
  }

  /* Front: brand side */
  .card--brand { background: var(--brand-blue); display: flex; }
  .brand__field { flex: 1; position: relative; }
  .brand__name {
    position: absolute; left: 36px; top: 58px; width: 290px;
    font-family: "Montserrat", sans-serif; font-weight: 800; font-size: 46px; line-height: 50px;
    color: var(--brand-yellow); text-transform: uppercase; letter-spacing: .5px;
  }
  .brand__rule { position: absolute; left: 38px; top: 172px; width: 240px; height: 2px; background: var(--paper); }
  .brand__cities {
    position: absolute; left: 38px; top: 188px;
    font-family: "Work Sans", sans-serif; font-weight: 500; font-size: 15px; line-height: 22px;
    color: var(--brand-orange);
  }
  .brand__stripes { width: 60px; height: 100%; }
  .brand__band--pink {
    width: 52px; background: var(--brand-pink); position: relative;
  }
  .brand__tagline {
    position: absolute; left: 50%; top: 50%;
    transform: translate(-50%, -50%) rotate(-90deg);
    white-space: nowrap;
    font-family: "Work Sans", sans-serif; font-weight: 500; font-size: 15px;
    color: var(--tagline-blue);
  }
  .brand__band--orange { width: 44px; background: var(--brand-orange); }
</style>
</head>
<body>
<main class="sheet">

  <section class="card card--contact" aria-label="Business card, contact side">
    <h1 class="contact__name">Marisol Vega</h1>
    <p class="contact__role">Founder &amp; Media Director</p>
    <span class="contact__rule-short"></span>
    <span class="contact__rule-long"></span>
    <p class="contact__lines">
      (305) 555-0147<br>
      marisol@LumenArcMedia.com<br>
      LumenArcMedia.com
    </p>
    <p class="contact__address">
      2400 Coral Way<br>
      4th Floor, Miami, FL 33145
    </p>
  </section>

  <section class="card card--brand" aria-label="Business card, brand side">
    <div class="brand__field">
      <h2 class="brand__name">Lumen Arc Media</h2>
      <span class="brand__rule"></span>
      <p class="brand__cities">
        Tampa • Boston •<br>
        Denver • Mérida • Napoli
      </p>
    </div>
    <svg class="brand__stripes" viewBox="0 0 60 303" preserveAspectRatio="none" aria-hidden="true">
      <rect width="60" height="303" fill="var(--deep-blue)"/>
      <g stroke="var(--stripe-blue)" stroke-width="1.4">
        <line x1="4" y1="0" x2="4" y2="303"/><line x1="10" y1="0" x2="10" y2="303"/>
        <line x1="16" y1="0" x2="16" y2="303"/><line x1="22" y1="0" x2="22" y2="303"/>
        <line x1="28" y1="0" x2="28" y2="303"/><line x1="34" y1="0" x2="34" y2="303"/>
        <line x1="40" y1="0" x2="40" y2="303"/><line x1="46" y1="0" x2="46" y2="303"/>
        <line x1="52" y1="0" x2="52" y2="303"/><line x1="58" y1="0" x2="58" y2="303"/>
      </g>
    </svg>
    <div class="brand__band--pink">
      <p class="brand__tagline">Framing Light. Telling Stories.</p>
    </div>
    <div class="brand__band--orange"></div>
  </section>

</main>
</body>
</html>
```